Re design and optimization of a website for pension Ora Vahi, a b&b in Tahiti, French Polynesia.

We have a website already : www.pensionoravahi.example

The general idea is to create a new site that is colorful, young and with an exotic, tropical feel since we are on a beautiful island.

The website will be in three languages, all the text is already available on our website, nothing changes.

All pages must have the name of the website (pension ora vahi b&b) our address, mail and phone number
It would be nice to have a link to our mail from every page

Sections have to be easy to update : text and pics

The sections needed are :

- Home page (accueil)

- Prices (tarifs)

- Bookings (reservations) = link to our mailbox : pensionoravahi@post.example )

- Pictures : in three separate categories that will pop up on this page : 1/ pics of the b&b 2/ pics of the surroundings 3/ customer's pics (we'll give new pics, not the current ones)

- Map of Tahiti : we'd like one map that we'll give you and also a Google map with our location, date and local time would be great

- Links (liens)

We let you see what would look best for the top banner and the switches, matching the logo and the pictures, make it nice and tropical !!
We have a few layouts that we did, maybe you will have a better idea of what we want by looking at them, if you can use them and have a good overall feel

We'd like to remind you guys that Tahiti is a dream destination, so you have to come up with something that the visitors will go : wow !!

We cater for backpackers to mid range accommodations and families, it all about a relaxed friendly atmosphere here !

NOTE THAT WE DON'T KNOW MUCH ABOUT PROGRAMMING AND CODING SO IT AS TO BE READY TO GO ON-LINE, ALL YOUR HELP IS APPRECIATED !!!
Also in Tahiti, the
INTERNET is quite low bandwidth so optimization is a must !

P.S : Live demo of the homepage is welcome ;)

We are available to all you for extra infos, good luck

regards,

remy & Pension Ora Vahi

Target Market(s)

Families and couples : individual rooms

Backpackers : Dormitories

people looking for an authentic stay in a familial environment

Customers of all ages and all nationalities

Requirements
Must have
• You must insist on the main page about :
the easy beach access
the breakfast included (with French baguette !)
Airport pick up 24/7
Many activities departing from our place : scuba diving, canyoning, 4x4 tour, rental cars, surf school, para-glide....

Please find a great way to highlight these !

```html
<!DOCTYPE html>
<html lang="en">
<head>
<meta charset="utf-8">
<title>Pension Ora Vahi – Bed and Breakfast, Tahiti</title>
<link href="https://fonts.googleapis.com/css2?family=PT+Sans:wght@400;700&family=Oswald:wght@300;400&display=swap" rel="stylesheet">
<style>
  :root{
    --orange:#f64a14;
    --orange-text:#f2501c;
    --ink:#222;
    --white:#fff;
    --line:#d8d8d8;
    --cream:#fff3c4;
  }
  *{box-sizing:border-box;margin:0;padding:0}
  html,body{width:1200px;height:1125px;overflow:hidden;background:var(--white)}
  body{position:relative;font-family:"PT Sans",Arial,sans-serif;color:var(--ink);font-size:12.5px}
  .site-header{position:absolute;left:0;top:0;width:1200px;height:110px;background:var(--orange)}
  .brand{position:absolute;left:155px;top:30px;font-size:38px;font-weight:700;color:#ffe100;line-height:1}
  .search{position:absolute;left:843px;top:21px;width:184px;height:23px;background:var(--white);display:flex;align-items:center;justify-content:space-between;padding:0 6px;font-size:11px;color:var(--orange-text)}
  .main-nav{position:absolute;right:170px;top:64px;display:flex;height:46px}
  .main-nav a{font-family:"Oswald",sans-serif;font-weight:300;font-size:17px;color:var(--white);text-decoration:none;padding:8px 13px 0;border-left:1px solid #c93a0c}
  .main-nav a:first-child{border-left:none}
  .hero{position:absolute;left:153px;top:111px;width:894px;height:289px;background:linear-gradient(180deg,#b7c9a8 0%,#4f7a2e 35%,#3f6e22 60%,#8dbb45 100%);box-shadow:0 18px 22px -10px rgba(0,0,0,.25)}
  .hero-arrow{position:absolute;top:126px}
  .panel{position:absolute;border:1px solid var(--line);background:var(--white);box-shadow:0 1px 3px rgba(0,0,0,.12)}
  .panel p,.list li{line-height:22px}
  .heading{color:var(--orange-text);font-size:16px;font-weight:400}
  .key{color:var(--orange-text);font-weight:700}
  .intro{left:151px;top:436px;width:470px;height:126px;padding:22px 17px}
  .badge-photo{position:absolute;border-radius:50%;border:5px dotted #fff;box-shadow:0 0 0 2px #e6e6e6}
  .breakfast{position:absolute;left:760px;top:429px;width:285px;height:124px;background:var(--orange);color:var(--white);padding:12px 24px;font-size:11px;line-height:16.5px}
  .breakfast h2{font-family:"Oswald",sans-serif;font-weight:300;font-style:italic;font-size:21px;line-height:28px;margin-bottom:4px}
  .breakfast strong{color:var(--cream);font-weight:700}
  .list{list-style:none}
  .list li{position:relative;padding-left:17px}
  .list li::before{content:"";position:absolute;left:2px;top:9px;border-left:4px solid var(--ink);border-top:3px solid transparent;border-bottom:3px solid transparent}
  .col{top:600px;height:208px;padding:14px 17px}
  .col-surf{left:150px;width:316px}
  .col-beach{left:476px;width:316px;padding:22px 14px 22px 21px}
  .col-beach p{white-space:nowrap;font-size:12px}
  .thumb{position:absolute;width:80px;height:111px}
  .houses{position:absolute;left:816px;top:595px;width:240px}
  .houses .list{margin-top:10px}
  .luggage{left:150px;top:838px;width:890px;height:147px;padding:20px 22px}
  .luggage-photo{position:absolute;right:8px;top:10px;width:177px;height:128px;background:linear-gradient(160deg,#4d7a33,#9cb887 50%,#6a4a3a)}
  .pickup{display:inline-block;margin-left:14px;padding:0 10px;background:var(--orange);color:var(--white);font-weight:700;font-size:14px;line-height:22px;border-radius:3px}
  .site-footer{position:absolute;left:0;top:997px;width:1200px;height:128px;background:var(--orange);color:var(--white);font-size:11px;line-height:18.5px}
  .footer-contact{position:absolute;left:149px;top:32px}
  .footer-nav{position:absolute;right:162px;top:32px;text-align:right}
  .site-footer a{color:var(--white);text-decoration:none}
</style>
</head>
<body>
<header class="site-header">
  <div class="brand">Pension Ora Vahi</div>
  <div class="search"><span>search</span>
    <svg width="18" height="18" viewBox="0 0 18 18"><circle cx="7" cy="7" r="5" fill="none" stroke="#999" stroke-width="1.6"/><line x1="11" y1="11" x2="16" y2="16" stroke="#999" stroke-width="2.4"/></svg>
  </div>
  <nav class="main-nav"><a href="#">Home</a><a href="#">Pricing</a><a href="#">Booking</a><a href="#">Photos</a></nav>
</header>

<div class="hero" role="img" aria-label="Tropical garden of the pension with white chairs, table and banana trees">
  <svg class="hero-arrow" style="left:22px" width="24" height="36" viewBox="0 0 24 36"><polyline points="20,2 4,18 20,34" fill="none" stroke="#fff" stroke-width="5"/></svg>
  <svg class="hero-arrow" style="right:24px" width="24" height="36" viewBox="0 0 24 36"><polyline points="4,2 20,18 4,34" fill="none" stroke="#fff" stroke-width="5"/></svg>
</div>

<section class="panel intro">
  <h1 class="heading">PENSION ORA VAHI - Bed and Breakfast</h1>
  <p>is located in the Paea district - 18,6 kms from Papeete - mountain<br>side. <span class="key">200 meters from the nicest white sand beach</span><br>of TAHITI French Polynesia</p>
</section>
<div class="badge-photo" style="left:527px;top:423px;width:134px;height:100px;background:radial-gradient(circle,#8cbf4a,#2f5a1c)" role="img" aria-label="Garden atmosphere of the pension"></div>
<div class="badge-photo" style="left:605px;top:482px;width:132px;height:99px;background:linear-gradient(180deg,#9cc7e8,#5a9ab8 45%,#d9d2b4 70%,#3f6e22)" role="img" aria-label="Beach access 200 metres from the pension"></div>

<aside class="breakfast">
  <h2>BED &amp; BREAKFAST</h2>
  <p>friendly atmosphere - <strong>breakfast included</strong><br><strong>with French baguette !</strong> every morning<br>at the garden terrace, 7h30 to 10h30<br>with a fantastic view at the mountain...</p>
</aside>

<section class="panel col col-surf">
  <p>accessible surf &nbsp;spots include :<br>Sapinus, mairie of Paea, Papara, Teahupoo...</p>
  <h2 class="heading" style="margin:8px 0 8px">Also departing from the pension</h2>
  <ul class="list"><li>scuba diving trips</li><li>canyoning</li><li>4WD tours of the island</li><li>surf school</li><li>paragliding</li></ul>
  <div class="thumb" style="left:228px;top:95px;background:linear-gradient(160deg,#4d7a33,#7da85a 50%,#b43a2a 75%,#4d6a2a)" role="img" aria-label="Tropical flowers in the garden"></div>
</section>

<section class="panel col col-beach">
  <p>Public beach &nbsp;with amenities only 200 meters away !<br>"Vaitea Park" also featuring :</p>
  <ul class="list" style="margin-top:20px"><li>restaurant - snack - bar</li><li>picnic area</li><li>kids play area</li><li>Ideal for snorkeling</li></ul>
  <div class="thumb" style="left:224px;top:95px;background:linear-gradient(90deg,#2a8bc7,#4aa8dc 60%,#6a4a3a)" role="img" aria-label="Bright blue room interior"></div>
</section>

<section class="houses">
  <h2 class="heading">LA PENSION ORA VAHI consists of<br>3 houses with</h2>
  <ul class="list">
    <li>1 Reception (tel - fax - internet)</li><li>5 rooms</li><li>2 dorms(4 beds in each)</li><li>communal bathrooms</li><li>télévision and library</li><li><span class="key">easy beach access</span> (at 200 meters away)</li>
    <li style="margin-top:8px;line-height:18.5px">cooking facilities (gas stoves, fridges,<br>micro-waves, plates and cutlery)</li>
  </ul>
</section>

<section class="panel luggage">
  <h2 class="heading">free luggage storage : upon the condition that you return to stay another night</h2>
  <p style="margin-top:8px">within proximity : &nbsp;rental cars and scooters, (Tahiti's cheapest), shops, supermarkets, snacks - restaurants médical center...</p>
  <p class="heading" style="margin-top:10px">TEL/FAX : (00 ) 55 01 23<span class="pickup">Airport pick up 24/7</span></p>
  <div class="luggage-photo" role="img" aria-label="Covered terrace with hammock and sofa"></div>
</section>

<footer class="site-footer">
  <div class="footer-contact">
    BP 100200 Punaauia 98700 Fare Nui TAHITI - French Polynesia<br>
    e mail : <a href="mailto:pensionoravahi@post.example">pensionoravahi@post.example</a><br>
    web side : www.pensionoravahi.example
  </div>
  <div class="footer-nav">
    <a href="#">Home</a> &nbsp;| &nbsp;<a href="#">Pricing</a> &nbsp;| &nbsp;<a href="#">Booking</a> &nbsp;| &nbsp;<a href="#">Photos</a><br>
    Copyrights @ 2012 All Rights Reserved
  </div>
</footer>
</body>
</html>
```